Updated Business Card Design more modern and eye catching

looking for something more dynamic than the sterile card we have now. Please take a look at our web site www.quarvinstores.net to see what we do. only looking for the front side of the card for now. I've also attached a sample of a card with raised spot uv ink - it might be cool to incorporate something like that. Card should be bold yet serious. No frilly or scrolly stuff on it.
Updates
Target Market(s)
We do decor and signage for retail business and supermarkets. Our new name should reflect that we're hip but serious.
Contact Information for Business Card
standard business card size - horizontal preferred
Font styles to use
Requirements
Must have
- Current logo and colors cannot be changed.
Nice to have
- Must have information shown on existing card but open to some changes. Okay to consider spot uv.
Should not have
- Not busy with pictures in the background.

```html
<!DOCTYPE html>
<html lang="en">
<head>
<meta charset="utf-8">
<title>Quarvin Stores – Business Card</title>
<link rel="stylesheet" href="https://fonts.googleapis.com/css2?family=Open+Sans:wght@400;600&family=Libre+Baskerville:ital@1&display=swap">
<style>
  :root {
    --backdrop: #2b2f36;
    --card-black: #1c1c1c;
    --gold: #c9b84a;
    --text-light: #e8e8e8;
    --text-muted: #bdbdbd;
  }
  * { margin: 0; padding: 0; box-sizing: border-box; }
  html, body {
    width: 1200px; height: 900px; overflow: hidden;
    background: var(--backdrop);
  }
  body { display: flex; align-items: center; justify-content: center; }
  .card {
    position: relative;
    width: 1000px; height: 572px;
    background: var(--card-black);
    border-radius: 40px;
    font-family: "Open Sans", sans-serif;
    color: var(--text-light);
    overflow: hidden;
  }
  .card__name {
    position: absolute; left: 70px; top: 160px;
    font-size: 38px; font-weight: 400; letter-spacing: 1px;
    line-height: 50px; text-transform: uppercase;
  }
  .card__title {
    position: absolute; left: 72px; top: 212px;
    font-family: "Libre Baskerville", serif; font-style: italic;
    font-size: 19px; line-height: 28px; color: var(--gold);
  }
  .card__rule {
    position: absolute; left: 240px; right: 0; top: 228px;
    height: 3px; background: var(--gold);
  }
  .contact {
    position: absolute; left: 70px; top: 262px;
    list-style: none;
  }
  .contact__item {
    display: flex; align-items: center; gap: 16px;
    font-size: 22px; line-height: 44px; color: var(--text-light);
  }
  .contact__icon { width: 22px; height: 22px; flex: none; }
  .brand {
    position: absolute; right: 70px; top: 150px;
    display: flex; align-items: center; gap: 18px;
  }
  .brand__mark {
    width: 50px; height: 50px;
    border: 3px solid var(--text-muted);
  }
  .brand__name {
    font-size: 46px; font-weight: 400; letter-spacing: 3px;
    line-height: 56px; text-transform: uppercase; color: var(--text-muted);
  }
  .address {
    position: absolute; right: 70px; bottom: 56px;
    list-style: none; text-align: right;
  }
  .address__item {
    display: flex; align-items: center; justify-content: flex-end; gap: 16px;
    font-size: 22px; line-height: 42px;
  }
  .address__item--plain { padding-right: 38px; }
</style>
</head>
<body>
  <article class="card">
    <h1 class="card__name">Marla Bennett</h1>
    <p class="card__title">Vice-President</p>
    <div class="card__rule"></div>

    <div class="brand">
      <span class="brand__mark"></span>
      <span class="brand__name">Quarvin Stores</span>
    </div>

    <ul class="contact">
      <li class="contact__item">
        <svg class="contact__icon" viewBox="0 0 24 24" fill="none" stroke="var(--gold)" stroke-width="2"><rect x="6" y="2" width="12" height="20" rx="2"/><line x1="10" y1="18" x2="14" y2="18"/></svg>
        555.310.4827
      </li>
      <li class="contact__item">
        <svg class="contact__icon" viewBox="0 0 24 24" fill="var(--gold)"><path d="M6.6 10.8a15 15 0 0 0 6.6 6.6l2.2-2.2c.3-.3.7-.4 1-.2 1.1.4 2.3.6 3.6.6.6 0 1 .4 1 1V20c0 .6-.4 1-1 1A17 17 0 0 1 3 4c0-.6.4-1 1-1h3.5c.6 0 1 .4 1 1 0 1.3.2 2.5.6 3.6.1.3 0 .7-.2 1z"/></svg>
        555.208.6190 ext.3
      </li>
      <li class="contact__item">
        <svg class="contact__icon" viewBox="0 0 24 24" fill="var(--gold)"><rect x="2" y="5" width="20" height="14" rx="1"/><path d="M3 6l9 7 9-7" fill="none" stroke="var(--card-black)" stroke-width="2"/></svg>
        Marla@quarvinStores.net
      </li>
    </ul>

    <ul class="address">
      <li class="address__item address__item--plain">4120 Commerce Way Dr.</li>
      <li class="address__item">
        Harbor Point, FL 30418
        <svg class="contact__icon" viewBox="0 0 24 24" fill="var(--gold)"><path d="M12 2a7 7 0 0 0-7 7c0 5 7 13 7 13s7-8 7-13a7 7 0 0 0-7-7zm0 9.5A2.5 2.5 0 1 1 12 6.5a2.5 2.5 0 0 1 0 5z"/></svg>
      </li>
      <li class="address__item">
        www.QuarvinStores.net
        <svg class="contact__icon" viewBox="0 0 24 24" fill="none" stroke="var(--text-muted)" stroke-width="1.6"><circle cx="12" cy="12" r="9"/><ellipse cx="12" cy="12" rx="4" ry="9"/><line x1="3" y1="12" x2="21" y2="12"/></svg>
      </li>
    </ul>
  </article>
</body>
</html>
```